Personal Business Card

Looking for a clean and modern personal business card. Basically I need something catchy to give to potential clients and people I meet. I do a lot of freelancing (from DJ'ing to wedding videography, but its mostly on the event side of things) so it's more-so about selling myself rather than identifying with a company. I'm starting to meet more people that I want to work with after meeting them so I'm revamping my business cards.

I'm looking for a clean and modern design- I know that's really vague but I'm fine with anything ranging from a symbol to just a fancy version of my name.

Details I need on the front:
Dennis Kowal
dennis@denniskowal-mail.net
(555) 807-2291

On the back I'd like to have something simple like "Nice to have met you today" or "Great meeting you".

UPDATE 9/27 Noon: My apologies for not putting it up before- I'm definitely looking for full color. Doesn't have to be a rainbow but I am looking for the least amount of blank white as possible.

UPDATE 10/1: Really impressed with what I've been getting so far and I'm working on giving everyone feedback- if your design is still up then you're still in the run. Looking for something more unique and modern so please do not post something that looks like a template from Cardloom!

Target Market(s)

Mainly to give to people aged 18-35. Most of my encounters will be casual so the card should have a "young" feeling to it. I rarely do anything in the corporate world so it doesn't have to be boring. It should give the impression that I'm the one they should go to if they need what I do (again it changes every weekend so I'll probably say the "what I do" part.

Industry/Entity Type

Wedding

Requirements
Must have
• Basically the contact information listed above
Nice to have
• I really like the colors Blue, Silver, and Purple. They don't have to necessarily all be there though. I do like the look of polished metal if that makes sense.
Should not have
• A template that resembles card-loom. I'm in a point in my life where I'm working a lot of different markets/areas so the card does not need to have an address or address placeholder.

```html
<!DOCTYPE html>
<html lang="en">
<head>
<meta charset="utf-8">
<title>Dennis Kowal – Business Card</title>
<link rel="stylesheet" href="https://fonts.googleapis.com/css2?family=Michroma&family=Arimo:wght@600&display=swap">
<style>
  :root {
    --card-black: #000000;
    --band-grey: #848282;
    --accent-olive: #a8a812;
    --page-white: #ffffff;
  }
  html, body {
    margin: 0;
    padding: 0;
    width: 1200px;
    height: 1000px;
    overflow: hidden;
    background: var(--page-white);
  }
  .sheet {
    position: relative;
    width: 1200px;
    height: 1000px;
  }
  .card {
    position: absolute;
    display: block;
    overflow: hidden;
  }
  .card--front-large { left: 69px; top: 65px; width: 1063px; height: 295px; }
  .card--back-large  { left: 70px; top: 393px; width: 1063px; height: 295px; }
  .card--front-small { left: 234px; top: 798px; width: 372px; height: 103px; }
  .card--back-small  { left: 610px; top: 798px; width: 372px; height: 103px; }

  .card .bg { fill: var(--card-black); }
  .card .band { fill: var(--band-grey); }
  .card .name-panel, .card .message-panel { fill: var(--card-black); }
  .card .accent-line { fill: var(--accent-olive); }
  .card .display-type {
    font-family: "Michroma", sans-serif;
    fill: var(--band-grey);
    stroke: var(--band-grey);
    stroke-width: 2.5;
  }
  .card .contact-type, .card .closing-type {
    font-family: "Michroma", sans-serif;
    fill: var(--card-black);
    stroke: var(--card-black);
  }
  .card .contact-type { stroke-width: 0.8; }
  .card .closing-type { stroke-width: 2.5; }

  .side-label {
    position: absolute;
    top: 900px;
    width: 300px;
    margin: 0;
    text-align: center;
    font-family: "Arimo", sans-serif;
    font-weight: 600;
    font-size: 52px;
    line-height: 64px;
    color: var(--card-black);
  }
  .side-label--front { left: 270px; }
  .side-label--back  { left: 645px; }
</style>
</head>
<body>
<main class="sheet">

  <!-- Front, large -->
  <svg class="card card--front-large" viewBox="0 0 1063 295" aria-label="Business card front">
    <rect class="bg" width="1063" height="295"/>
    <path class="band" d="M0 28 H991 a10 10 0 0 1 10 10 V258 a10 10 0 0 1 -10 10 H0 Z"/>
    <rect class="name-panel" x="547" y="45" width="560" height="166" rx="10"/>
    <text class="display-type" x="624" y="113" textLength="428" lengthAdjust="spacingAndGlyphs"><tspan font-size="82">D</tspan><tspan font-size="64">ENNIS</tspan></text>
    <text class="display-type" x="559" y="210" textLength="494" lengthAdjust="spacingAndGlyphs"><tspan font-size="82">K</tspan><tspan font-size="64">OWAL</tspan></text>
    <rect class="accent-line" x="0" y="222" width="1063" height="3"/>
    <text class="contact-type" x="21" y="262" font-size="22" textLength="605" lengthAdjust="spacingAndGlyphs">DENNIS@DENNISKOWAL-MAIL.NET</text>
    <text class="contact-type" x="658" y="260" font-size="24" textLength="325" lengthAdjust="spacingAndGlyphs">(555)807-2291</text>
  </svg>

  <!-- Back, large -->
  <svg class="card card--back-large" viewBox="0 0 1063 295" aria-label="Business card back">
    <rect class="bg" width="1063" height="295"/>
    <path class="band" d="M63 28 H1053 a10 10 0 0 1 10 10 V259 a10 10 0 0 1 -10 10 H63 Z"/>
    <rect class="message-panel" x="-20" y="45" width="567" height="166" rx="10"/>
    <text class="display-type" x="343" y="89" font-size="54" textLength="197" lengthAdjust="spacingAndGlyphs">NICE</text>
    <text class="display-type" x="177" y="148" font-size="54" textLength="363" lengthAdjust="spacingAndGlyphs">TO HAVE</text>
    <text class="display-type" x="323" y="209" font-size="54" textLength="219" lengthAdjust="spacingAndGlyphs">MEET</text>
    <rect class="accent-line" x="0" y="222" width="1063" height="3"/>
    <text class="closing-type" x="63" y="265" font-size="46" textLength="479" lengthAdjust="spacingAndGlyphs">YOU TODAY</text>
  </svg>

  <!-- Front, small -->
  <svg class="card card--front-small" viewBox="0 0 1063 295" aria-label="Business card front, preview">
    <rect class="bg" width="1063" height="295"/>
    <path class="band" d="M0 28 H991 a10 10 0 0 1 10 10 V258 a10 10 0 0 1 -10 10 H0 Z"/>
    <rect class="name-panel" x="547" y="45" width="560" height="166" rx="10"/>
    <text class="display-type" x="624" y="113" textLength="428" lengthAdjust="spacingAndGlyphs"><tspan font-size="82">D</tspan><tspan font-size="64">ENNIS</tspan></text>
    <text class="display-type" x="559" y="210" textLength="494" lengthAdjust="spacingAndGlyphs"><tspan font-size="82">K</tspan><tspan font-size="64">OWAL</tspan></text>
    <rect class="accent-line" x="0" y="222" width="1063" height="3"/>
    <text class="contact-type" x="21" y="262" font-size="22" textLength="605" lengthAdjust="spacingAndGlyphs">DENNIS@DENNISKOWAL-MAIL.NET</text>
    <text class="contact-type" x="658" y="260" font-size="24" textLength="325" lengthAdjust="spacingAndGlyphs">(555)807-2291</text>
  </svg>

  <!-- Back, small -->
  <svg class="card card--back-small" viewBox="0 0 1063 295" aria-label="Business card back, preview">
    <rect class="bg" width="1063" height="295"/>
    <path class="band" d="M63 28 H1053 a10 10 0 0 1 10 10 V259 a10 10 0 0 1 -10 10 H63 Z"/>
    <rect class="message-panel" x="-20" y="45" width="567" height="166" rx="10"/>
    <text class="display-type" x="343" y="89" font-size="54" textLength="197" lengthAdjust="spacingAndGlyphs">NICE</text>
    <text class="display-type" x="177" y="148" font-size="54" textLength="363" lengthAdjust="spacingAndGlyphs">TO HAVE</text>
    <text class="display-type" x="323" y="209" font-size="54" textLength="219" lengthAdjust="spacingAndGlyphs">MEET</text>
    <rect class="accent-line" x="0" y="222" width="1063" height="3"/>
    <text class="closing-type" x="63" y="265" font-size="46" textLength="479" lengthAdjust="spacingAndGlyphs">YOU TODAY</text>
  </svg>

  <p class="side-label side-label--front">Front</p>
  <p class="side-label side-label--back">Back</p>
</main>
</body>
</html>
```